IRON SASH VIGOUR CERTIFICATE

Corvane Kickfist Inc is wanting to introduce a fitness system based upon certificates reflecting rank; White - Yellow - Blue - Red - Black.

The Certificate "MUST" have on it "IRON SASH VIGOUR"

The Certificate "MUST" have a martial arts theme!

The Certificate "MUST" reflect the fitness requirements for each rank.

The colour scheme for each Certificate "MUST" reflect the belt rank

The Certificate must include at least one martial arts graphic / motif

The certificate must have the Corvane KKF LOGO

We will need a certificate template that can be for all levels but reflect the rank and fitness level. The certificate can be either traditional or modern style but must reflect a martial art themes. The certificate must have the Corvane Kickfist logo incorporated into the certificate with signature space for senior instructors Gus Pelham & Nessa Crail-Pelham. The certificates should be eye catching and exciting to look at. It should bold and incorporate martial art motifs etc The fitness requirements are not onerous and the certificate system is created to incentivise physical activity and correct technique rather than creating an impossible standards only Olympians can achieve. The majority of our students are upper primary and lower secondary from 11yr-15yrs. Certificate should be youthful but not silly. The certificate template will be reproduced for each colour belt.White = 10 push ups 10 Sit ups 10 squats 10 Jumping Jacks 20 sec plank 400m continuous run Demonstrate beginner stretching techniqueYellow = 20 push ups 20 sit ups 20 squats 20 Jumping Jacks 40 Sec plank 800m continuous run Demonstrate intermediate stretching techniqueBlue = 30 push ups 30 sit ups 30 squats 30 Jumping Jacks 60 Sec plank 1200m continuous run Demonstrate intermediate stretching techniqueRed = 40 push ups 40 sit ups 40 squats 40 Jumping Jacks 75sec plank 1600m run Demonstrate advanced stretching techniqueBlack = 50 push ups 50 sit ups 50 squats 50 Jumping jacks 90 sec planks 2000m continuous run Demonstrate advanced stretching technique
Updates

HI Designers, Please go for modern and professionals. Several designs have used traditional motifs of water dragons or lattice bordering. This looks old school. Please do not use martial art silhouettes as it looks amateur. Definately looking for upmarket high quality presentations.

Logo Text

IRON SASH VIGOUR

Font styles to use
Decorative

Colors

Designer to choose colors to be used in the design.

Requirements
Must have
• This will be a template foe all coloured ranks of fitness, Be bold, memorable, should be themed to martial arts etc

```html
<!DOCTYPE html>
<html lang="en">
<head>
<meta charset="utf-8">
<title>Corvane Kickfist – Iron Sash Vigour Certificates</title>
<link rel="stylesheet" href="https://fonts.googleapis.com/css2?family=Barlow+Condensed:wght@700&family=Montserrat:wght@300;400;500;700;800&display=swap">
<style>
  :root {
    --navy: #262b3d;
    --ink: #1d2130;
    --paper: #ffffff;
    --paper-shade: #eceef1;
    --belt-red: #e31e24;
    --belt-black: #1d2130;
    --belt-yellow: #e8b92e;
    --belt-white: #b9b9bb;
    --belt-blue: #1631d8;
  }
  * { box-sizing: border-box; margin: 0; padding: 0; }
  html, body { width: 794px; height: 1200px; overflow: hidden; background: #fff; }
  body { position: relative; font-family: "Montserrat", sans-serif; color: var(--ink); }

  .slot { position: absolute; }
  .slot--hero { left: 17px; top: 41px; width: 752px; height: 531px; }
  .slot--small { width: 372px; height: 263px; }
  .slot--small .certificate { transform: scale(0.4947); transform-origin: 0 0; }
  .slot--r1 { top: 614px; } .slot--r2 { top: 889px; }
  .slot--c1 { left: 21px; } .slot--c2 { left: 401px; }

  .certificate {
    position: absolute; left: 0; top: 0; width: 752px; height: 531px; overflow: hidden;
    background:
      linear-gradient(135deg, rgba(0,0,0,0.03) 25%, transparent 25%) 0 0 / 90px 90px,
      linear-gradient(225deg, rgba(0,0,0,0.025) 25%, transparent 25%) 0 0 / 90px 90px,
      radial-gradient(circle at 55% 45%, var(--paper) 40%, var(--paper-shade) 100%);
    box-shadow: 0 4px 14px rgba(0,0,0,0.35);
  }
  .certificate--red { --accent: var(--belt-red); --label: var(--belt-red); }
  .certificate--black { --accent: var(--belt-black); --label: var(--ink); }
  .certificate--yellow { --accent: var(--belt-yellow); --label: var(--belt-yellow); }
  .certificate--white { --accent: var(--belt-white); --label: var(--ink); }
  .certificate--blue { --accent: var(--belt-blue); --label: var(--belt-blue); }

  .corner-art { position: absolute; inset: 0; width: 752px; height: 531px; }
  .corner-art .dark { fill: var(--navy); }
  .corner-art .streak { fill: var(--accent); }

  .kicker-art {
    position: absolute; left: 24px; top: 16px; width: 180px; height: 390px;
    border-radius: 40% 60% 30% 50% / 30% 40% 60% 70%;
    background: linear-gradient(160deg, var(--navy) 0%, var(--accent) 60%, rgba(255,255,255,0) 100%);
    opacity: 0.8;
  }

  .title { position: absolute; right: 92px; top: 62px; text-align: right; }
  .title__lead { font-weight: 400; font-size: 39px; letter-spacing: 1px; line-height: 1; color: var(--ink); }
  .title__main {
    font-family: "Barlow Condensed", sans-serif; font-weight: 700; font-size: 104px; line-height: 0.9;
    letter-spacing: -1px; margin-top: 2px;
    background: linear-gradient(180deg, var(--ink) 0%, var(--ink) 38%, var(--accent) 62%, var(--accent) 100%);
    -webkit-background-clip: text; background-clip: text; color: transparent;
  }

  .program {
    position: absolute; left: 218px; width: 482px; top: 232px; text-align: center;
    font-weight: 700; font-size: 15px; letter-spacing: 6px; color: var(--label);
  }

  .divider { position: absolute; left: 218px; top: 269px; width: 482px; border-top: 2px solid var(--ink); }

  .rank {
    position: absolute; left: 218px; width: 482px; top: 282px; text-align: center;
    font-weight: 800; font-size: 44px; line-height: 1.1; letter-spacing: -1px; color: var(--label);
  }

  .requirements {
    position: absolute; left: 218px; width: 482px; top: 342px; list-style: none;
    display: flex; flex-wrap: wrap; justify-content: center; column-gap: 14px; row-gap: 6px;
    font-size: 14px; font-weight: 400; color: var(--ink); white-space: nowrap;
  }
  .requirements li::before {
    content: ""; display: inline-block; width: 9px; height: 9px; margin-right: 5px;
    border: 1.5px solid var(--accent); border-radius: 2px;
  }

  .signature { position: absolute; top: 454px; width: 180px; text-align: center; border-top: 2px solid var(--ink); padding-top: 8px; }
  .signature--left { left: 73px; } .signature--right { left: 441px; }
  .signature__name { font-weight: 700; font-size: 15px; text-transform: uppercase; letter-spacing: -0.2px; white-space: nowrap; }
  .signature__role { font-weight: 400; font-size: 13px; margin-top: 2px; }

  .club-mark { position: absolute; left: 297px; top: 420px; width: 100px; text-align: center; }
  .club-mark__dot { display: block; width: 52px; height: 52px; margin: 0 auto 4px; border-radius: 50%; background: var(--navy); }
  .club-mark__name { font-weight: 700; font-size: 13px; color: var(--navy); white-space: nowrap; }
</style>
</head>
<body>

<!-- Red belt (featured) -->
<div class="slot slot--hero">
  <section class="certificate certificate--red">
    <svg class="corner-art" viewBox="0 0 752 531" aria-hidden="true">
      <polygon class="dark" points="480,0 752,0 752,300 738,215 690,95 600,28"/>
      <polygon class="streak" points="560,0 610,0 705,55 742,150 752,230 732,175 692,80"/>
      <polygon class="dark" points="752,330 752,531 470,531 610,505 700,445"/>
      <polygon class="streak" points="752,360 752,400 705,480 600,531 555,531 690,470"/>
    </svg>
    <div class="kicker-art" role="img" aria-label="Flaming martial artist kicking, illustration area"></div>
    <header class="title"><p class="title__lead">CERTIFICATE OF</p><h1 class="title__main">FITNESS</h1></header>
    <p class="program">IRON SASH VIGOUR</p>
    <div class="divider"></div>
    <h2 class="rank">RED BELT</h2>
    <ul class="requirements">
      <li>40 Push Ups</li><li>40 Sit Ups</li><li>40 Squats</li><li>40 Jumping Jacks</li>
      <li>75sec Plank</li><li>1600m Run</li><li>Advanced Stretching</li>
    </ul>
    <div class="signature signature--left"><p class="signature__name">Gus Pelham</p><p class="signature__role">Senior Instructor</p></div>
    <div class="club-mark"><span class="club-mark__dot"></span><span class="club-mark__name">Corvane KKF</span></div>
    <div class="signature signature--right"><p class="signature__name">Nessa Crail-Pelham</p><p class="signature__role">Senior Instructor</p></div>
  </section>
</div>

<!-- Black belt -->
<div class="slot slot--small slot--r1 slot--c1">
  <section class="certificate certificate--black">
    <svg class="corner-art" viewBox="0 0 752 531" aria-hidden="true">
      <polygon class="dark" points="480,0 752,0 752,300 738,215 690,95 600,28"/>
      <polygon class="streak" points="560,0 610,0 705,55 742,150 752,230 732,175 692,80"/>
      <polygon class="dark" points="752,330 752,531 470,531 610,505 700,445"/>
      <polygon class="streak" points="752,360 752,400 705,480 600,531 555,531 690,470"/>
    </svg>
    <div class="kicker-art" role="img" aria-label="Flaming martial artist kicking, illustration area"></div>
    <header class="title"><p class="title__lead">CERTIFICATE OF</p><h1 class="title__main">FITNESS</h1></header>
    <p class="program">IRON SASH VIGOUR</p>
    <div class="divider"></div>
    <h2 class="rank">BLACK BELT</h2>
    <ul class="requirements">
      <li>50 Push Ups</li><li>50 Sit Ups</li><li>50 Squats</li><li>50 Jumping Jacks</li>
      <li>90sec Plank</li><li>2000m Run</li><li>Advanced Stretching</li>
    </ul>
    <div class="signature signature--left"><p class="signature__name">Gus Pelham</p><p class="signature__role">Senior Instructor</p></div>
    <div class="club-mark"><span class="club-mark__dot"></span><span class="club-mark__name">Corvane KKF</span></div>
    <div class="signature signature--right"><p class="signature__name">Nessa Crail-Pelham</p><p class="signature__role">Senior Instructor</p></div>
  </section>
</div>

<!-- Yellow belt -->
<div class="slot slot--small slot--r1 slot--c2">
  <section class="certificate certificate--yellow">
    <svg class="corner-art" viewBox="0 0 752 531" aria-hidden="true">
      <polygon class="dark" points="480,0 752,0 752,300 738,215 690,95 600,28"/>
      <polygon class="streak" points="560,0 610,0 705,55 742,150 752,230 732,175 692,80"/>
      <polygon class="dark" points="752,330 752,531 470,531 610,505 700,445"/>
      <polygon class="streak" points="752,360 752,400 705,480 600,531 555,531 690,470"/>
    </svg>
    <div class="kicker-art" role="img" aria-label="Flaming martial artist kicking, illustration area"></div>
    <header class="title"><p class="title__lead">CERTIFICATE OF</p><h1 class="title__main">FITNESS</h1></header>
    <p class="program">IRON SASH VIGOUR</p>
    <div class="divider"></div>
    <h2 class="rank">YELLOW BELT</h2>
    <ul class="requirements">
      <li>20 Push Ups</li><li>20 Sit Ups</li><li>20 Squats</li><li>20 Jumping Jacks</li>
      <li>40sec Plank</li><li>800m Run</li><li>Intermediate Stretching</li>
    </ul>
    <div class="signature signature--left"><p class="signature__name">Gus Pelham</p><p class="signature__role">Senior Instructor</p></div>
    <div class="club-mark"><span class="club-mark__dot"></span><span class="club-mark__name">Corvane KKF</span></div>
    <div class="signature signature--right"><p class="signature__name">Nessa Crail-Pelham</p><p class="signature__role">Senior Instructor</p></div>
  </section>
</div>

<!-- White belt -->
<div class="slot slot--small slot--r2 slot--c1">
  <section class="certificate certificate--white">
    <svg class="corner-art" viewBox="0 0 752 531" aria-hidden="true">
      <polygon class="dark" points="480,0 752,0 752,300 738,215 690,95 600,28"/>
      <polygon class="streak" points="560,0 610,0 705,55 742,150 752,230 732,175 692,80"/>
      <polygon class="dark" points="752,330 752,531 470,531 610,505 700,445"/>
      <polygon class="streak" points="752,360 752,400 705,480 600,531 555,531 690,470"/>
    </svg>
    <div class="kicker-art" role="img" aria-label="Flaming martial artist kicking, illustration area"></div>
    <header class="title"><p class="title__lead">CERTIFICATE OF</p><h1 class="title__main">FITNESS</h1></header>
    <p class="program">IRON SASH VIGOUR</p>
    <div class="divider"></div>
    <h2 class="rank">WHITE BELT</h2>
    <ul class="requirements">
      <li>10 Push Ups</li><li>10 Sit Ups</li><li>10 Squats</li><li>10 Jumping Jacks</li>
      <li>20sec Plank</li><li>400m Run</li><li>Beginner Stretching</li>
    </ul>
    <div class="signature signature--left"><p class="signature__name">Gus Pelham</p><p class="signature__role">Senior Instructor</p></div>
    <div class="club-mark"><span class="club-mark__dot"></span><span class="club-mark__name">Corvane KKF</span></div>
    <div class="signature signature--right"><p class="signature__name">Nessa Crail-Pelham</p><p class="signature__role">Senior Instructor</p></div>
  </section>
</div>

<!-- Blue belt -->
<div class="slot slot--small slot--r2 slot--c2">
  <section class="certificate certificate--blue">
    <svg class="corner-art" viewBox="0 0 752 531" aria-hidden="true">
      <polygon class="dark" points="480,0 752,0 752,300 738,215 690,95 600,28"/>
      <polygon class="streak" points="560,0 610,0 705,55 742,150 752,230 732,175 692,80"/>
      <polygon class="dark" points="752,330 752,531 470,531 610,505 700,445"/>
      <polygon class="streak" points="752,360 752,400 705,480 600,531 555,531 690,470"/>
    </svg>
    <div class="kicker-art" role="img" aria-label="Flaming martial artist kicking, illustration area"></div>
    <header class="title"><p class="title__lead">CERTIFICATE OF</p><h1 class="title__main">FITNESS</h1></header>
    <p class="program">IRON SASH VIGOUR</p>
    <div class="divider"></div>
    <h2 class="rank">BLUE BELT</h2>
    <ul class="requirements">
      <li>30 Push Ups</li><li>30 Sit Ups</li><li>30 Squats</li><li>30 Jumping Jacks</li>
      <li>60sec Plank</li><li>1200m Run</li><li>Intermediate Stretching</li>
    </ul>
    <div class="signature signature--left"><p class="signature__name">Gus Pelham</p><p class="signature__role">Senior Instructor</p></div>
    <div class="club-mark"><span class="club-mark__dot"></span><span class="club-mark__name">Corvane KKF</span></div>
    <div class="signature signature--right"><p class="signature__name">Nessa Crail-Pelham</p><p class="signature__role">Senior Instructor</p></div>
  </section>
</div>

</body>
</html>
```